Flyer for an online formula one racing league

Hello.

I am looking for the perfect one page facebook/instagram style flyer for an online formula one racing league. The racing league is called 'VOLTA RACING LEAGUE'.

Information that MUST be on the new flyer is already on the old flyer I have uploaded here. In addition to including: The Volta racing league 'V' logo I have uploaded AND the text: 'Very popular, clean and competitive racing league, running for its 4th season. Why not join with a friend? Race times, Mondays, Tuesdays and Wednesdays each at 8pm UK TIME Message below for any questions. (Spacing of information is not important, however all the information in regards to the racing I have just mentioned MUST BE on the flyer, this includes info from old pic, logo and the other info I just mentioned).

It would be beneficial to have lots of dark blue on the flyer and the new flyer to be a lot different to the original flyer I uploaded, but this is not essential.

I apologise if I did not explain very well, any questions, please message me.

The best flyer should look the most attractive to someone that might be interested in joining an online formula one racing league.

I used this website before to create the perfect logo for my Sunday League team last year, and I was very impressed. I look forward to seeing your submissions.

Target Market(s)

No specific target, more something that may attract someone into joining a formula one online racing league

Industry/Entity Type

e sports/formula one

Colors
0054AA
0677BA
7BADD7
CADEEF
E8F1F8

Requirements
Must have
• Read product description please
Should not have
• Ignoring product description!

```html
<!DOCTYPE html>
<html lang="en">
<head>
<meta charset="utf-8">
<title>Volta Racing League – New Season</title>
<link rel="stylesheet" href="https://fonts.googleapis.com/css2?family=Lexend:wght@300;400;600;700&display=swap">
<style>
  :root {
    --navy: #171a4a;
    --navy-deep: #12143a;
    --navy-soft: #24285e;
    --stripe: #1c2052;
    --pink: #c2066f;
    --sky: #7badd7;
    --white: #ffffff;
  }
  html, body {
    margin: 0;
    padding: 0;
    width: 1200px;
    height: 620px;
    overflow: hidden;
    background: var(--navy);
  }
  .flyer {
    position: relative;
    width: 1200px;
    height: 620px;
    overflow: hidden;
    background: var(--navy);
    font-family: "Lexend", "Helvetica Neue", Arial, sans-serif;
    color: var(--white);
  }
  .backdrop {
    position: absolute;
    inset: 0;
  }
  .car-photo {
    position: absolute;
    left: 120px;
    top: 190px;
    width: 1080px;
    height: 340px;
    background: radial-gradient(ellipse at 62% 50%, rgba(120,128,170,0.42) 0%, rgba(60,66,115,0.28) 45%, rgba(23,26,74,0) 75%);
  }
  .brand-mark {
    position: absolute;
    left: 50px;
    top: 58px;
    width: 204px;
    height: 204px;
    border-radius: 50%;
    background: var(--navy-deep);
    display: flex;
    align-items: center;
    justify-content: center;
    font-weight: 700;
    font-size: 38px;
    color: var(--white);
  }
  .league-name {
    position: absolute;
    left: 280px;
    top: 64px;
    margin: 0;
    font-size: 43px;
    font-weight: 600;
    line-height: 1;
  }
  .running-line {
    position: absolute;
    left: 280px;
    top: 133px;
    margin: 0;
    font-size: 22px;
    font-weight: 300;
    line-height: 1;
  }
  .accent-bar {
    position: absolute;
    left: 497px;
    top: 137px;
    width: 703px;
    height: 15px;
    background: var(--pink);
  }
  .year {
    position: absolute;
    left: 274px;
    top: 172px;
    margin: 0;
    font-size: 86px;
    font-weight: 700;
    letter-spacing: 2px;
    line-height: 1;
  }
  .details {
    position: absolute;
    left: 0;
    top: 354px;
    width: 1200px;
    text-align: center;
    margin: 0;
    padding: 0;
    list-style: none;
  }
  .details li {
    font-size: 26px;
    font-weight: 300;
    letter-spacing: 2.6px;
    line-height: 47px;
  }
  .details .highlight {
    font-weight: 600;
    letter-spacing: 1px;
  }
  .availability {
    position: absolute;
    left: 0;
    top: 516px;
    width: 1200px;
    margin: 0;
    text-align: center;
    font-size: 42px;
    font-weight: 600;
    letter-spacing: 0.8px;
    line-height: 1.2;
  }
  .race-info {
    position: absolute;
    left: 0;
    top: 582px;
    width: 1200px;
    margin: 0;
    text-align: center;
    font-size: 17px;
    font-weight: 400;
    letter-spacing: 1px;
    line-height: 1.2;
    color: var(--sky);
  }
  .race-info strong {
    color: var(--white);
    font-weight: 600;
  }
  .race-info .sep {
    color: var(--pink);
    padding: 0 10px;
  }
</style>
</head>
<body>
<main class="flyer">
  <svg class="backdrop" width="1200" height="620" viewBox="0 0 1200 620" aria-hidden="true">
    <g fill="var(--stripe)">
      <rect x="0" y="0" width="1200" height="6"/>
      <rect x="0" y="18" width="1200" height="8"/>
      <rect x="0" y="40" width="1200" height="6"/>
    </g>
    <path d="M0 620 L0 560 C 200 520 320 500 470 470 L 470 620 Z" fill="var(--navy-soft)" opacity="0.7"/>
  </svg>

  <div class="car-photo" role="img" aria-label="Photo of a formula one car racing on track, faded into the background"></div>

  <svg class="backdrop" width="1200" height="620" viewBox="0 0 1200 620" aria-hidden="true">
    <path d="M745 350 C 725 270 800 212 1000 194 C 1100 188 1170 200 1200 210 L1200 245 C 1100 220 905 240 808 292 C 778 308 760 328 745 350 Z" fill="var(--pink)"/>
  </svg>

  <div class="brand-mark">VOLTA</div>

  <h1 class="league-name">VOLTA RACING LEAGUE</h1>
  <p class="running-line">RUNNING FOR ITS</p>
  <div class="accent-bar"></div>
  <p class="year">4TH YEAR</p>

  <ul class="details">
    <li class="highlight">NEW SEASON JUST STARTING</li>
    <li>CLEAN ONLINE RACING LEAGUE</li>
    <li>3 DIVISIONS CURRENTLY AND LOOKING TO KEEP GROWING</li>
  </ul>

  <p class="availability">Spaces Left on Monday, Tuesdays &amp; Wednesdays</p>

  <p class="race-info"><strong>Races at 8pm UK time</strong><span class="sep">•</span>Why not join with a friend?<span class="sep">•</span>Message below for any questions</p>
</main>
</body>
</html>
```